New Brochure Design Project for Tavu/Velmora App development company

we need a brochure for a company in uk which develops Korvix and Velmora application.

Also company specialise in Quillbrook deployment and Software applications.

The brochure is need for Lumigrid exhibition which is taking place in Nov

Also need a page on Recruitment which shows that company can provide candidates for Tavu and Velmora

Target Market(s)

All domain

Industry/Entity Type

It Company

Font styles to use
Serif
Sans Serif
Decorative
Script

Colors
f04a50
0355a3
faee3e
f78f1f
a44599

Requirements
Must have
• Mobile pictures and nice graphics

```html
<!DOCTYPE html>
<html lang="en">
<head>
<meta charset="utf-8">
<title>BYTEHAVEN Brochure</title>
<link href="https://fonts.googleapis.com/css2?family=Open+Sans:ital,wght@0,300;0,400;0,600;0,700;0,800;1,400;1,600&display=swap" rel="stylesheet">
<style>
:root{
  --red:#e8502e;--yellow:#f5a623;--purple:#8b2a8b;--blue:#1f3e9e;--green:#8cc63f;--teal:#2aa89a;
  --brand-blue:#0355a3;--sky:#7ec7ec;--light-grey:#c9c9c9;--ink:#222;--mark-grey:#6d6d6d;--sep:#cfcfcf;
}
*{margin:0;padding:0;box-sizing:border-box}
html,body{width:769px;height:1200px;overflow:hidden;background:#fff}
body{position:relative;font-family:"Open Sans",Arial,sans-serif;color:var(--ink)}
.abs{position:absolute}
.art{position:absolute}
.sheet-gap{position:absolute;left:0;top:597px;width:769px;height:8px;background:#e6e6e6}
.fold{position:absolute;left:385px;width:1px;background:var(--sep)}
/* back panel */
.contact{position:absolute;left:0;width:376px;text-align:center;font-size:7.5px;font-weight:700;color:#777;line-height:1.15}
.dot{position:absolute;width:20px;height:20px;border-radius:50%;left:178px}
.dot svg{width:20px;height:20px;display:block}
.wordmark{font-weight:800;color:var(--mark-grey);white-space:nowrap}
/* tiles */
.tile{position:absolute;width:161px;height:43px;color:#fff;display:flex;align-items:center;padding-left:12px;gap:10px;font-size:12.5px;line-height:1.05;font-weight:800;text-transform:uppercase}
.tile i{font-weight:400}
.tile svg{width:26px;height:26px;flex:none}
/* services */
.services h2{font-size:25px;font-weight:600;color:var(--ink)}
.svc{position:absolute;left:18px;width:210px}
.svc h3{font-size:7.5px;font-weight:600;color:#444;margin-bottom:2px}
.svc p{font-size:6px;line-height:1.3;color:#222}
.svc .bold{font-weight:700;font-style:italic}
.tags{display:flex;gap:3px;margin:3px 0}
.tags span{background:var(--green);color:#fff;font-size:7.5px;font-weight:700;padding:2px 5px}
.rule{border-top:1px dashed #bbb;margin-top:4px}
.hire{position:absolute;left:244px;width:140px}
.hire .big{font-size:19px;line-height:1.0;color:var(--ink)}
.adv{background:var(--teal);color:#fff;font-size:12px;font-weight:700;padding:2px 0 2px 8px;margin:6px 0 8px;letter-spacing:.5px}
.hire h4{font-size:13px;font-weight:700;margin-top:6px}
.hire p{font-size:5.6px;color:#555;font-style:italic;line-height:1.3}
.circle{position:absolute;border-radius:50%;color:#fff;font-size:6.5px;font-weight:800;display:flex;align-items:center;justify-content:center}
.tech{position:absolute;font-size:15.5px;font-weight:800;color:var(--light-grey);line-height:.95}
/* inside right */
.r-h{font-size:9px;font-weight:800}
.r-sub{font-size:6px;font-style:italic;color:#555}
table.qa{position:absolute;left:396px;top:665px;width:230px;border-collapse:collapse;font-size:5px}
table.qa th{background:#444;color:#fff;font-weight:600;padding:3px 2px;text-align:left;height:22px}
table.qa td{vertical-align:top;padding:3px 2px;border-right:1px solid #999;border-bottom:1px solid #999;font-style:italic;line-height:1.15;height:64px}
.tick{display:inline-block;width:8px;height:8px;border-radius:50%;background:var(--green);vertical-align:middle;margin-right:2px}
.steps{position:absolute;left:397px;top:782px;display:flex}
.steps span{background:var(--green);color:#fff;font-size:6.5px;font-weight:700;padding:2px 9px 2px 7px;clip-path:polygon(0 0,88% 0,100% 50%,88% 100%,0 100%,8% 50%)}
.mini{font-size:5.5px;line-height:1.25;color:#333}
.seo-item{position:absolute;width:118px;font-size:7.5px;font-weight:700;line-height:1.1}
.seo-item b{color:var(--green);font-size:12px;margin-right:2px}
.seo-item small{display:block;font-size:5.5px;font-weight:400;font-style:italic;color:#555;margin-left:10px;line-height:1.25}
.recruit{position:absolute;left:405px;width:350px;font-size:5.8px;line-height:1.35;color:#333}
.recruit h5{color:var(--brand-blue);font-size:6px;font-weight:700;margin-top:7px}
</style>
</head>
<body>

<!-- ===== Outside: back panel ===== -->
<div class="art" role="img" aria-label="Cluster of colourful overlapping circles holding digital service icons" style="left:88px;top:12px;width:205px;height:188px;border-radius:50%;background:radial-gradient(circle at 45% 45%,#f5a623 0%,#e8502e 35%,#8b2a8b 60%,#2aa89a 80%,#fff 100%)"></div>

<div class="dot" style="top:208px;background:var(--yellow)"><svg viewBox="0 0 20 20"><path d="M10 4a4 4 0 0 0-4 4c0 3 4 8 4 8s4-5 4-8a4 4 0 0 0-4-4z" fill="#fff"/><circle cx="10" cy="8" r="1.5" fill="#f5a623"/></svg></div>
<div class="contact" style="top:238px">BYTEHAVEN<br>14 Harrow Court,<br>9-11 Marden Lane<br>Elmsworth Essex<br>EL42QT</div>
<div class="contact" style="top:286px">CONTACT : DANIEL OKORO</div>
<div class="dot" style="top:305px;background:var(--green)"><svg viewBox="0 0 20 20"><rect x="5" y="7" width="10" height="7" fill="#fff"/><path d="M5 7l5 4 5-4" stroke="#8cc63f" fill="none"/></svg></div>
<div class="contact" style="top:330px;font-weight:600">daniel@bytehavenltd.com<br>info@bytehavenltd.com<br>maya@bytehavenltd.com</div>
<div class="dot" style="top:364px;background:var(--purple)"><svg viewBox="0 0 20 20"><rect x="7" y="4" width="6" height="12" rx="1" fill="#fff"/></svg></div>
<div class="contact" style="top:391px;font-weight:600">02070000147<br>07700900482</div>
<div class="dot" style="top:419px;background:var(--green)"><svg viewBox="0 0 20 20"><text x="10" y="14" font-size="11" text-anchor="middle" fill="#fff" font-weight="700">@</text></svg></div>
<div class="contact" style="top:446px">www.bytehavenltd.com</div>

<div class="art" role="img" aria-label="Hand holding a phone receiver linked by cord to a globe with mail and chat icons" style="left:0;top:478px;width:270px;height:105px;background:linear-gradient(90deg,#8fb8e8 0%,#f5a623 40%,#6fb0d8 75%,#f4f4f4 100%)"></div>
<div class="art" role="img" aria-label="Old desk telephone" style="left:272px;top:525px;width:90px;height:58px;background:linear-gradient(90deg,#f4f4f4 0%,#555 40%,#222 100%)"></div>
<div class="abs wordmark" style="left:276px;top:492px;font-size:14px;display:flex;align-items:center;gap:4px"><span style="width:10px;height:10px;border-radius:50%;background:var(--sky)"></span>BYTEHAVEN</div>

<div class="fold" style="top:0;height:597px"></div>

<!-- ===== Outside: cover ===== -->
<div class="abs" style="left:480px;top:30px;width:170px;text-align:center">
  <div style="width:48px;height:48px;border-radius:50%;background:var(--sky);margin:0 auto 18px"></div>
  <div class="wordmark" style="font-size:26px">BYTEHAVEN</div>
</div>
<div class="art" role="img" aria-label="Hand pointing up to a cloud of speech bubbles with colourful app and web icons" style="left:395px;top:160px;width:370px;height:437px;background:radial-gradient(ellipse at 50% 40%,#e8502e 0%,#f5a623 30%,#8b2a8b 55%,#2aa89a 72%,#fff 92%)"></div>

<div class="sheet-gap"></div>

<!-- ===== Inside: services panel ===== -->
<div class="tile" style="left:30px;top:628px;background:var(--red)"><svg viewBox="0 0 26 26"><circle cx="13" cy="13" r="11" fill="none" stroke="#fff" stroke-width="2"/><path d="M2 13h22M13 2c-5 6-5 16 0 22M13 2c5 6 5 16 0 22" stroke="#fff" fill="none" stroke-width="1.5"/></svg><span>Web <i>Design</i><br>&amp; <i>Develpment</i></span></div>
<div class="tile" style="left:194px;top:628px;background:var(--yellow)"><svg viewBox="0 0 26 26"><rect x="3" y="6" width="20" height="13" fill="none" stroke="#fff" stroke-width="2"/><path d="M1 21h24" stroke="#fff" stroke-width="2"/></svg><span>Mobile <i>&amp;</i><br><i>Tablet Apps</i></span></div>
<div class="tile" style="left:30px;top:676px;background:var(--purple)"><svg viewBox="0 0 26 26"><path d="M3 22V16M8 22V12M13 22V9M18 22V6M3 12l6-5 5 3 9-7" stroke="#fff" stroke-width="2.5" fill="none"/></svg><span>SEO, <i>PPC &amp; SMM</i></span></div>
<div class="tile" style="left:194px;top:676px;background:var(--blue)"><svg viewBox="0 0 26 26"><circle cx="11" cy="11" r="7" fill="none" stroke="#fff" stroke-width="2.5"/><path d="M16 16l7 7" stroke="#fff" stroke-width="3"/></svg><span>QA <i>&amp; Testing</i></span></div>
<div class="tile" style="left:30px;top:724px;background:var(--green)"><svg viewBox="0 0 26 26"><circle cx="7" cy="9" r="3" fill="#fff"/><circle cx="19" cy="9" r="3" fill="#fff"/><circle cx="13" cy="8" r="3.5" fill="#fff"/><path d="M2 20c0-5 10-5 10 0M14 20c0-5 10-5 10 0M7 20c0-6 12-6 12 0" fill="#fff"/></svg><span>Offshore &amp;<br>Onsite <i>Staffing</i></span></div>
<div class="tile" style="left:194px;top:724px;background:var(--teal)"><svg viewBox="0 0 26 26"><circle cx="10" cy="13" r="6" fill="none" stroke="#fff" stroke-width="3" stroke-dasharray="3 2"/><circle cx="20" cy="19" r="3" fill="none" stroke="#fff" stroke-width="2"/></svg><span>Software<br><i>Development</i></span></div>

<div class="abs" style="left:0;top:790px;width:385px;border-top:1px dashed #bbb"></div>
<div class="abs" style="left:233px;top:795px;height:300px;border-left:1px solid #999"></div>

<div class="abs services" style="left:18px;top:800px"><h2>Services</h2></div>

<div class="svc" style="top:839px">
  <h3>Custom Application Development</h3>
  <div class="tags"><span>Web</span><span>Mobile</span><span>Desktop</span><span>Cloud</span></div>
  <p class="bold">We are masters in all the leading technologies &amp; platforms. So we can provide you with the best technical solution for your business needs.</p>
  <div class="rule"></div>
</div>
<div class="svc" style="top:895px">
  <h3>Content Management System (CMS)</h3>
  <p><i>Custom Development<br>Open Source Implementation / Customization</i></p>
  <div class="tags"><span>Pressleaf</span><span>Droplane</span><span>Jovella</span><span>NetNimbus</span></div>
  <p><i>Maintenance &amp; Support</i></p>
  <div class="rule"></div>
</div>
<div class="svc" style="top:964px">
  <h3>e-Commerce Solutions</h3>
  <p><i>Custom Development<br>Open Source Implementation / Customization</i></p>
  <div class="tags"><span>Magnova</span><span>Opalcart</span><span>Orbcommerce</span></div>
  <p><i>Maintenance &amp; Support</i></p>
  <div class="rule"></div>
</div>
<div class="svc" style="top:1034px">
  <h3>Business Solutions</h3>
  <p><i>ERP, CRM, Document Management System, Inventory Management, HRMS, MIS, etc.</i></p>
  <div class="rule"></div>
</div>
<div class="svc" style="top:1070px">
  <h3>Independent QA &amp; Testing</h3>
  <p><i>Manual as well as Automated software testing services.</i></p>
</div>

<div class="hire" style="top:801px">
  <div class="big">Hire<br><b>Dedicated</b><br>Team</div>
  <div class="adv">ADVANTAGES</div>
  <h4>Low Cost</h4><p>Save almost 70% compared to traditional inhouse staffing.</p>
  <h4>Scrable</h4><p>Flexibility to scale up OR down based on your business needs without any overheads.</p>
  <h4>Flexibility</h4><p>Hire full time, part time OR hourly per your business needs.</p>
  <h4>No Hidden Cost</h4><p>The services is simple; a resource fee without any overheads</p>
  <h4>On demand</h4><p>Hire resources as and when required as per your business needs.</p>
</div>
<div class="circle" style="left:240px;top:1084px;width:48px;height:48px;background:var(--purple)">OFFSHORE</div>
<div class="circle" style="left:281px;top:1084px;width:42px;height:42px;background:#e0245e">ONSITE</div>
<div class="circle" style="left:324px;top:1084px;width:46px;height:46px;background:var(--green)">HYBRID</div>

<div class="abs" style="left:0;top:1095px;width:233px;height:5px;background:#e6e6e6"></div>
<div class="tech" style="left:18px;top:1116px">NORTHSOFT<br>OPEN SOURSE<br>FRAMEWORKS<br>KOVA</div>
<div class="tech" style="left:152px;top:1116px">WEB<br>MOBILE<br>DATABASES<br>UI/UX</div>

<div class="fold" style="top:605px;height:595px"></div>

<!-- ===== Inside: QA / UX / SEO / recruitment ===== -->
<div class="abs" style="left:397px;top:617px">
  <div class="r-h">INDEPENDENT QA &amp; TESTING</div>
  <div class="r-sub">Benefits of 3rd Party Testing</div>
</div>
<div class="abs mini" style="left:397px;top:644px;width:94px;border-bottom:1px solid #333"><i>Unbiased Testing<br>Better Quality, End-User Satisfaction</i></div>
<div class="abs mini" style="left:494px;top:644px;width:76px;background:#e6e6e6"><i>High Savings in Cost &amp; Time<br>Low Risk, Higher Reliability</i></div>

<table class="qa">
  <tr><th><span class="tick"></span>Core Testing Services</th><th><span class="tick"></span>Specialized Testing Services</th><th><span class="tick"></span>QA &amp; Test Consultancy</th></tr>
  <tr>
    <td>• Functional testing<br>• User acceptance testing<br>• Performance (Load/Stress) testing<br>• Security testing<br>• System (End-to-end) testing</td>
    <td>• Mobile testing (Tavu, Velmora, Panes &amp; others)<br>• Cross browser testing (Edgeway, Chroma, Foxfire, Savanna)<br>• Cross Platform testing (Panes, Tern/Lynx, Orchard OS)<br>• Game testing<br>• Database testing<br>• Device testing</td>
    <td>• Test strategy design<br>• Test process assessment and improvement<br>• Quality audits<br>• Coaching</td>
  </tr>
</table>

<div class="art" role="img" aria-label="Smartphone surrounded by colourful app icons" style="left:640px;top:628px;width:125px;height:215px;background:radial-gradient(circle at 50% 30%,#f5a623 0%,#e8502e 25%,#8cc63f 45%,#5a5a5a 70%,#fff 100%)"></div>

<div class="abs" style="left:397px;top:761px;font-size:5px;font-weight:700">MANUAL &amp; AUTOMATED TESTING · MANAGED TEST CENTER/LAB (WITH 10+ PROFESSIONALS)</div>
<div class="abs" style="left:397px;top:767px;font-size:11px;font-weight:700">UI / UX (Design Services)</div>
<div class="steps"><span>Requirements</span><span>Concept</span><span>Designs</span><span>Validation</span></div>
<div class="abs mini" style="left:403px;top:800px">Web UI / UX<br>Mobile UI/UX<br>Corporate Branding</div>
<div class="abs mini" style="left:463px;top:800px">PSD to HTML Conversion<br>HTML5/CSS3 Development<br>Responsive Design Implementation</div>

<div class="abs" style="left:403px;top:823px;font-size:11px;font-weight:700">SEO SERVICES</div>
<div class="seo-item" style="left:397px;top:840px"><b>1</b>Search Engine Optimization<small>Searchly, Findr &amp; Yodel</small></div>
<div class="seo-item" style="left:518px;top:840px"><b>3</b>Social Media Optimization<small>Friendwall, Chirpline, Linkwork &amp; Circles</small></div>
<div class="seo-item" style="left:397px;top:860px"><b>2</b>Pay Per Click<small>Searchly adwords, Northsoft adCenter &amp; Yodel Search Marketing</small></div>
<div class="seo-item" style="left:518px;top:860px"><b>4</b>Content Writing<small>Keyword Rich &amp; SEO Friendly</small></div>

<div class="abs" style="left:684px;top:887px;font-size:11px;font-weight:800;color:var(--brand-blue)">BYTEHAVEN</div>
<div class="abs" style="left:405px;top:893px;font-size:19px;font-weight:700;color:var(--brand-blue)">RECRUITMENT SERVICES</div>

<div class="recruit" style="top:938px">
  <p>We provide the full range of recruitment services; from the sourcing of local talent to the deployment of international teams.</p>
  <h5>Contract Recruitment</h5>
  <p>With immediate access to our Global Network of Enterprise Technology contractors, we provide a fast and flexible delivery model that enables the deployment of consultants with specific technical and language skills. We ensure full contractor compliance including eligibility and local tax, and can arrange flights and accommodation as per each assignment.</p>
  <h5>Project Solutions</h5>
  <p>Our team based resourcing model enables our clients to source local project teams for multi-national rollouts, whilst maintaining full control over the success, cost and delivery of their projects. On your behalf, BYTEHAVEN will forge a team of best-in-class consultants at a significant cost reduction to that of a Consulting Partner or Systems Integrator.</p>
  <h5>Permanent Recruitment</h5>
  <p>We take the time to identify, qualify and engage with candidates whose technical, cultural and career objectives are perfectly in line with your own. For each assignment, we will perform a detailed search of our Global Network and deliver country specific advertising and media campaigns.</p>
  <h5>Executive Search</h5>
  <p>Selecting the best is a matter of judgement. We evaluate the top talent for your business by seamlessly integrating in-depth market research with our vast practical experience. Through headhunting and networking with industry specialists, we aim to target and secure the best talent for your business within 2 weeks of assignment qualification.</p>
</div>

<div class="art" role="img" aria-label="Photo of a business professional at work" style="left:386px;top:1102px;width:146px;height:98px;background:linear-gradient(135deg,#dfe6ee 0%,#b9c3cf 50%,#5b6470 100%)"></div>

</body>
</html>
```